Jade Pan Kitchen Chinese Takeaway Menu

We need the new menu design for our Jade Pan Kitchen chinese takeaway menu as all the resources are had been uploaded all of the photos must be in the menu,
Need a Dish Runner and Chatterly Logo on the Jade pan kitchen logo page
OPEN 7 DAYS Sun-Thu 10.00am - 9.00pm Fri-Sat 10.00am - 9.30pm
Shop 9, Marlowe Arcade 512 Keller St, Ashgrove QLD 4810
Phone: 07 4715 3362
The best fresh food around- no MSG used, and all dishes low in fat! YOU CAN ALSO MAKE YOUR OWN DISHES
Delivery in 3km radius, 5:00-9:00pm each day (charge applies). Prices effective June 2017. All prices inclusive of G.S.T. Prices subject to change.
Need space for another 9 Photos

I had been increase my Budget and want to get more designs to submit, the logo of DishRunner you can google it on the site, and i had been update the Brief, Please check it carefully, Thank you Added Thursday, June 22, 2017

Target Market(s)

Winner will invite to design the menu board

Industry/Entity Type

Inn

Font styles to use
Serif

Colors

Designer to choose colors to be used in the design.

Requirements
Must have
• Need a DishRunner and Chatterly Logo
• OPEN 7 DAYS Sun-Thu 10.00am - 9.00pm Fri-Sat 10.00am - 9.30pm
• Shop 9, Marlowe Arcade 512 Keller St, Ashgrove QLD 4810
• Phone: 07 4715 3362
• The best fresh food around- no MSG used, and all dishes low in fat! YOU CAN ALSO MAKE YOUR OWN DISHES
• Delivery in 3km radius, 5:00-9:00pm each day (charge applies). Prices effective June 2017. All prices inclusive of G.S.T. Prices subject to change.
• Need space for another 9 Photos
Nice to have
• Totally 58 Photos

```html
<!DOCTYPE html>
<html lang="en">
<head>
<meta charset="utf-8">
<title>Jade Pan Kitchen — Takeaway Menu</title>
<link href="https://fonts.googleapis.com/css2?family=Open+Sans:wght@300;400;600;700&family=Oswald:wght@300;500&display=swap" rel="stylesheet">
<style>
:root{
  --red:#e31e26;
  --red-dark:#c2151c;
  --ink:#333;
  --muted:#666;
  --paper:#fff;
  --stage:#ececec;
  --food-warm:#d9a27a;
  --food-green:#9bb974;
}
*{box-sizing:border-box;margin:0;padding:0}
html,body{width:1200px;height:1200px;overflow:hidden}
body{background:var(--stage);font-family:"Open Sans",sans-serif;color:var(--ink)}
.brochure{position:absolute;left:20px;top:215px;width:1160px;height:770px;display:grid;grid-template-columns:repeat(4,290px);background:var(--paper);border-top:5px solid var(--red);box-shadow:0 8px 24px rgba(0,0,0,.18)}
.panel{position:relative;overflow:hidden;border-right:1px solid #e4e4e4}
.panel:last-child{border-right:none}
.backdrop{position:absolute;inset:0;background:linear-gradient(160deg,#f3d7c2 0%,#e8b896 35%,#d6c9a6 60%,#c9d6b0 100%);opacity:.55}
.panel-inner{position:relative;padding:14px 14px}
/* menu list */
.dish{display:grid;grid-template-columns:1fr 42px 40px;gap:4px;align-items:center;height:47px;border-bottom:1px solid rgba(0,0,0,.08)}
.dish-name{font-size:8.5px;font-weight:700;color:var(--red)}
.dish-desc{font-size:7.5px;color:var(--ink);line-height:1.25}
.dish-price{font-size:8.5px;font-weight:600;color:var(--red);text-align:right;align-self:start;padding-top:4px}
.thumb{width:36px;height:36px;border:2px solid #fff;box-shadow:0 1px 3px rgba(0,0,0,.25);background:linear-gradient(135deg,var(--food-warm),#a5532e 60%,var(--food-green))}
/* section ribbons */
.ribbon{display:block;width:150px;margin:6px auto 8px;background:var(--red);color:#fff;text-align:center;font-size:8.5px;font-weight:600;letter-spacing:.5px;padding:3px 0;clip-path:polygon(0 0,100% 0,94% 50%,100% 100%,0 100%,6% 50%)}
.entree{list-style:none;font-size:8px;margin:0 6px 14px}
.entree li{display:flex;align-items:baseline;gap:4px;line-height:1.45}
.entree .leader{flex:1;border-bottom:1px dotted #888}
.entree .cost{color:var(--red);min-width:80px}
/* photos panel */
.photo-grid{display:grid;grid-template-columns:repeat(3,1fr);gap:10px;padding:16px 16px 0}
.photo-grid .thumb{width:100%;height:56px;border-width:3px}
.brand{font-family:"Open Sans",sans-serif;font-weight:700;color:var(--red);font-size:20px;letter-spacing:-.3px;display:flex;align-items:center;gap:7px}
.brand-dot{width:14px;height:14px;border-radius:50%;background:var(--red)}
.hours{text-align:center;margin-top:18px}
.hours .brand{justify-content:center}
.clock{display:block;margin:12px auto 6px}
.open{color:var(--red);font-weight:700;font-size:13px}
.times{font-size:10px;line-height:1.5}
.contact{position:absolute;left:0;right:0;bottom:0;height:318px;background:var(--red);color:#fff;padding:26px 22px}
.contact h2{font-size:14px;font-weight:700;border-bottom:1px solid #fff;padding-bottom:4px;margin-bottom:8px}
.phone{font-size:20px;font-weight:700}
.address{font-size:10px;font-weight:600;line-height:1.45;padding-bottom:12px;border-bottom:1px solid #fff;margin-bottom:12px}
.terms{font-size:10px;line-height:1.5;font-weight:600}
.terms p+p{margin-top:10px}
.join{display:flex;align-items:center;gap:6px;margin-top:14px;font-size:10px;font-weight:700}
.join-dot{width:12px;height:12px;border-radius:50%;background:#fff}
/* cover */
.cover .brand{justify-content:center;margin-top:24px;font-size:24px}
.tagline{margin:26px 22px 0;font-family:"Oswald",sans-serif;font-weight:300;font-size:17px;line-height:1.2;color:#444}
.tagline .q{color:var(--red);font-weight:500}
.tagline .hl{color:var(--red)}
.tagline .strong{font-weight:500;color:#222}
.hero{margin:20px 0 0 20px;height:270px;border-radius:140px 0 0 140px;background:radial-gradient(circle at 45% 50%,#7a3a1e 0%,#a4582f 35%,#e2b15a 60%,#7fa24a 80%,#f2efe9 100%)}
.make{position:absolute;bottom:44px;left:0;right:0;text-align:center;font-family:"Oswald",sans-serif;line-height:1.1}
.make .light{font-weight:300;font-size:19px;color:#555}
.make .bold{font-weight:500;font-size:27px;color:var(--red)}
</style>
</head>
<body>
<main class="brochure">

  <section class="panel menu-mains">
    <div class="backdrop" role="img" aria-label="Faded photo of a plated stir-fry dish behind the menu"></div>
    <div class="panel-inner">
      <div class="dish"><div><div class="dish-name">11. Honey Prawn</div><div class="dish-desc">Battered King Prawns tossed with Honey &amp; Sesame Seeds on steamed rice</div></div><div class="dish-price">$16.90</div><div class="thumb" role="img" aria-label="Honey prawn photo"></div></div>
      <div class="dish"><div><div class="dish-name">12. General Tso's Chicken</div><div class="dish-desc">Marinated pieces of Crispy Chicken in a Spicy &amp; Sweet sauce on steamed rice</div></div><div class="dish-price">$14.50</div><div class="thumb" role="img" aria-label="General Tso's chicken photo"></div></div>
      <div class="dish"><div><div class="dish-name">13. Sesame Chicken</div><div class="dish-desc">Marinated pieces of Crispy Chicken with Broccoli &amp; Sesame seeds served on steamed rice</div></div><div class="dish-price">$14.50</div><div class="thumb" role="img" aria-label="Sesame chicken photo"></div></div>
      <div class="dish"><div><div class="dish-name">14. House Family</div><div class="dish-desc">Delicious combo Meat &amp; Seafood with Seasonal Vegetables in House Sauce on steamed rice</div></div><div class="dish-price">$16.90</div><div class="thumb" role="img" aria-label="Family combo photo"></div></div>
      <div class="dish"><div><div class="dish-name">15. Garlic Fish Fillet</div><div class="dish-desc">Deep Fried Fish Fillet with Vegetables in a Garlic Oyster Sauce served with steamed rice</div></div><div class="dish-price">$14.50</div><div class="thumb" role="img" aria-label="Garlic fish fillet photo"></div></div>
      <div class="dish"><div><div class="dish-name">16. Honey Pepper Steak</div><div class="dish-desc">Honey Pepper Steak pieces with Seasonal Vegetables served on steamed rice</div></div><div class="dish-price">$14.50</div><div class="thumb" role="img" aria-label="Honey pepper steak photo"></div></div>
      <div class="dish"><div><div class="dish-name">17. Deep Fried Prawn with Spicy Salt</div><div class="dish-desc">Deep Fried Prawn with Spicy Salt Sauce on steamed rice</div></div><div class="dish-price">$16.90</div><div class="thumb" role="img" aria-label="Spicy salt prawn photo"></div></div>
      <div class="dish"><div><div class="dish-name">18. Crispy Chicken</div><div class="dish-desc">Crispy Chicken with Thai Sweet Chilli Sauce on steamed rice</div></div><div class="dish-price">$13.90</div><div class="thumb" role="img" aria-label="Crispy chicken photo"></div></div>
      <div class="dish"><div><div class="dish-name">19. Shanghai Steak</div><div class="dish-desc">Shanghai Steak pieces with Seasonal Vegetables served on steamed rice</div></div><div class="dish-price">$14.50</div><div class="thumb" role="img" aria-label="Shanghai steak photo"></div></div>
      <div class="dish"><div><div class="dish-name">20. Honey Soy Chicken</div><div class="dish-desc">Chicken and Seasonal Vegetables with Honey Soy Sauce on steamed rice</div></div><div class="dish-price">$13.90</div><div class="thumb" role="img" aria-label="Honey soy chicken photo"></div></div>
      <div class="dish"><div><div class="dish-name">21. Teriyaki Chicken</div><div class="dish-desc">Chicken and Seasonal Vegetables with Teriyaki Sauce on steamed rice</div></div><div class="dish-price">$13.90</div><div class="thumb" role="img" aria-label="Teriyaki chicken photo"></div></div>
      <div class="dish"><div><div class="dish-name">22. SzeChuan Spicy Beef</div><div class="dish-desc">Beef and Seasonal Vegetables with SzeChuan Spicy Sauce on steamed rice</div></div><div class="dish-price">$13.90</div><div class="thumb" role="img" aria-label="SzeChuan beef photo"></div></div>
      <div class="dish"><div><div class="dish-name">23. Japanese Curry Katsu</div><div class="dish-desc">Crispy Pork fillet with Japanese Curry on steamed rice</div></div><div class="dish-price">$13.90</div><div class="thumb" role="img" aria-label="Curry katsu photo"></div></div>
      <div class="dish"><div><div class="dish-name">24. Japanese Curry Chicken</div><div class="dish-desc">Chicken pieces with Japanese Curry on steamed rice</div></div><div class="dish-price">$13.90</div><div class="thumb" role="img" aria-label="Curry chicken photo"></div></div>
      <div class="dish"><div><div class="dish-name">25. House Omelette</div><div class="dish-desc">Omelette with delicious Combo Meat &amp; Seasonal Vegetables. Steamed rice optional</div></div><div class="dish-price">$15.50</div><div class="thumb" role="img" aria-label="Omelette photo"></div></div>
    </div>
  </section>

  <section class="panel menu-rice">
    <div class="backdrop" role="img" aria-label="Faded photo of fresh vegetables behind the menu"></div>
    <div class="panel-inner">
      <span class="ribbon">ENTREE</span>
      <ul class="entree">
        <li>Spring Rolls<span class="leader"></span><span class="cost">$1.50ea / $5.00 4pk</span></li>
        <li>Dim Sims<span class="leader"></span><span class="cost">$2.00ea / $6.00 4pk</span></li>
        <li>Tempura Prawns<span class="leader"></span><span class="cost">$2.20ea / $8.00 4pk</span></li>
        <li>Prawn Chips<span class="leader"></span><span class="cost">$2.50 bag</span></li>
        <li>Crispy Noodles<span class="leader"></span><span class="cost">$2.00</span></li>
        <li>Miso Soup<span class="leader"></span><span class="cost">$3.00</span></li>
        <li>Chicken Corn Soup<span class="leader"></span><span class="cost">$5.00</span></li>
      </ul>
      <span class="ribbon">HOUSE FRIED RICE</span>
      <div class="dish"><div><div class="dish-name">1. House Special Fried Rice</div><div class="dish-desc">Traditional rice with Shrimps, Roast Pork &amp; Vegetables</div></div><div class="dish-price">$11.90</div><div class="thumb" role="img" aria-label="Special fried rice photo"></div></div>
      <div class="dish"><div><div class="dish-name">2. Sambal Fried Rice</div><div class="dish-desc">Malaysian style rice with Chicken &amp; Vegetables in Sambal Sauce</div></div><div class="dish-price">$11.90</div><div class="thumb" role="img" aria-label="Sambal fried rice photo"></div></div>
      <div class="dish"><div><div class="dish-name">3. Nasi Goreng</div><div class="dish-desc">Malaysian style rice dish with Roast Pork &amp; Vegetables</div></div><div class="dish-price">$11.90</div><div class="thumb" role="img" aria-label="Nasi goreng photo"></div></div>
      <div class="dish"><div><div class="dish-name">4. Seafood Nasi Goreng</div><div class="dish-desc">Malaysian style rice dish with mixed Seafood &amp; Vegetables</div></div><div class="dish-price">$13.90</div><div class="thumb" role="img" aria-label="Seafood nasi goreng photo"></div></div>
      <div class="dish"><div><div class="dish-name">5. Teppan Fried Rice</div><div class="dish-desc">Traditional rice with Shrimps, Bacon, Eggs &amp; Vegetables in a Dark Soy Sauce</div></div><div class="dish-price">$12.90</div><div class="thumb" role="img" aria-label="Teppan fried rice photo"></div></div>
      <span class="ribbon">STEAMED RICE</span>
      <div class="dish"><div><div class="dish-name">6. Creamy Garlic King Prawn</div><div class="dish-desc">King Prawns with Creamy Garlic Sauce served on a bed of steamed rice</div></div><div class="dish-price">$16.90</div><div class="thumb" role="img" aria-label="Garlic king prawn photo"></div></div>
      <div class="dish"><div><div class="dish-name">7. Honey / Lemon Chicken</div><div class="dish-desc">Battered Chicken in a Honey or Lemon Sauce</div></div><div class="dish-price">$13.90</div><div class="thumb" role="img" aria-label="Lemon chicken photo"></div></div>
      <div class="dish"><div><div class="dish-name">8. Cashew Nut Chicken</div><div class="dish-desc">Chicken served with Cashew Nuts, Seasonal Vegetables on rice</div></div><div class="dish-price">$13.90</div><div class="thumb" role="img" aria-label="Cashew chicken photo"></div></div>
      <div class="dish"><div><div class="dish-name">9. Sweet &amp; Sour Chicken/Pork</div><div class="dish-desc">Battered Pork/Chicken with Pineapple, Carrots &amp; Capsicum in Sweet &amp; Sour Sauce</div></div><div class="dish-price">$13.90</div><div class="thumb" role="img" aria-label="Sweet and sour photo"></div></div>
      <div class="dish"><div><div class="dish-name">10. Rainbow Beef</div><div class="dish-desc">Battered Beef with Carrots, Onion &amp; Capsicum in Sweet &amp; Sour Sauce on rice</div></div><div class="dish-price">$13.90</div><div class="thumb" role="img" aria-label="Rainbow beef photo"></div></div>
    </div>
  </section>

  <section class="panel info">
    <div class="photo-grid">
      <div class="thumb" role="img" aria-label="Dish photo"></div><div class="thumb" role="img" aria-label="Dish photo"></div><div class="thumb" role="img" aria-label="Dish photo"></div>
      <div class="thumb" role="img" aria-label="Dish photo"></div><div class="thumb" role="img" aria-label="Dish photo"></div><div class="thumb" role="img" aria-label="Dish photo"></div>
      <div class="thumb" role="img" aria-label="Dish photo"></div><div class="thumb" role="img" aria-label="Dish photo"></div><div class="thumb" role="img" aria-label="Dish photo"></div>
    </div>
    <div class="hours">
      <div class="brand"><span class="brand-dot"></span>Jade pan kitchen</div>
      <svg class="clock" width="26" height="26" viewBox="0 0 26 26" aria-hidden="true"><circle cx="13" cy="13" r="11" fill="none" stroke="#888" stroke-width="2.5"/><path d="M13 7v6h5" fill="none" stroke="#888" stroke-width="2.5" stroke-linecap="round"/></svg>
      <div class="open">OPEN 7 DAYS</div>
      <div class="times">Sun-Thu 10.00am - 9.00pm<br>Fri-Sat 10.00am - 9.30pm</div>
    </div>
    <div class="contact">
      <h2>Contact Information</h2>
      <div class="phone">07 4715 3362</div>
      <div class="address">Shop 9, Marlowe Arcade<br>512 Keller St,<br>Ashgrove QLD 4810</div>
      <div class="terms">
        <p>Delivery in 3km radius, 5:00-9:00pm each day (charge applies).</p>
        <p>Prices effective June 2017.<br>All prices inclusive of G.S.T.<br>Prices subject to change</p>
      </div>
      <div class="join"><span class="join-dot"></span>Join Us</div>
    </div>
  </section>

  <section class="panel cover">
    <div class="brand"><span class="brand-dot"></span>Jade pan kitchen</div>
    <p class="tagline"><span class="q">“</span> The best fresh food<br>&amp; all dishes <span class="hl">low in fat!</span><br><span class="strong">AROUND NO <span class="hl">MSG</span> USED</span> <span class="q">”</span></p>
    <div class="hero" role="img" aria-label="Bowl of beef stir-fry noodles with broccoli and spring onion"></div>
    <div class="make"><div class="light">YOU CAN ALSO MAKE</div><div class="bold">YOUR OWN DISHES</div></div>
  </section>

</main>
</body>
</html>
```